Bramblewick Gardening Services. A6 flyer single sided

Need an A6 flyer designing. Single sided.
I am a gardener.
I do lawn mowing - one-off garden tidy ups or regular fortnightly visits.
All kinds of trees expertly felled, topped or pruned.
Hedge cutting.
Fencing replaced or repaired.
Fully insured.
Access to fully qualified and licenced tree arborist
07724 316048 or 01632 742918.

I have attached my business card and letter head logo.
I'm open to new designs without incorporating any of my artwork.

Industry/Entity Type

Gardener

```html
<!DOCTYPE html>
<html lang="en">
<head>
<meta charset="utf-8">
<title>Bramblewick Garden Services – Flyer</title>
<link rel="stylesheet" href="https://fonts.googleapis.com/css2?family=Roboto+Slab:wght@800&family=Open+Sans:wght@600;700&family=Roboto:wght@700;900&display=swap">
<style>
  :root {
    --grass-light: #6cbd3c;
    --grass-mid: #4fa12c;
    --grass-dark: #2f7a1e;
    --band-green: #0f6b35;
    --panel-tint: rgba(190, 235, 215, 0.55);
    --panel-edge: rgba(255, 255, 255, 0.35);
    --ink: #111a12;
    --white: #ffffff;
    --hedge-light: #7fae3a;
    --hedge-dark: #2c5314;
  }
  html, body {
    margin: 0;
    padding: 0;
    width: 946px;
    height: 1200px;
    overflow: hidden;
    background: #e9ece6;
  }
  .flyer {
    position: relative;
    width: 946px;
    height: 1200px;
    overflow: hidden;
    background: radial-gradient(ellipse at 50% 35%, var(--grass-light) 0%, var(--grass-mid) 55%, var(--grass-dark) 100%);
    font-family: "Open Sans", sans-serif;
  }
  .brand-title {
    position: absolute;
    top: 26px;
    left: 0;
    width: 100%;
    margin: 0;
    text-align: center;
    font-family: "Roboto Slab", serif;
    font-weight: 800;
    font-size: 70px;
    line-height: 88px;
    color: var(--white);
    text-shadow: 0 2px 4px rgba(0, 0, 0, 0.35);
  }
  .tagline-band {
    position: absolute;
    top: 218px;
    left: 0;
    width: 100%;
    height: 54px;
    background: var(--band-green);
    color: var(--white);
    font-family: "Roboto", sans-serif;
    font-weight: 700;
    font-size: 36px;
    line-height: 54px;
    text-align: center;
  }
  .info-panel {
    position: absolute;
    top: 296px;
    left: 26px;
    width: 894px;
    height: 760px;
    border-radius: 26px;
    background: var(--panel-tint);
    border: 2px solid var(--panel-edge);
    box-sizing: border-box;
  }
  .services-heading {
    position: absolute;
    top: 14px;
    left: 30px;
    margin: 0;
    font-weight: 600;
    font-size: 36px;
    line-height: 50px;
    color: var(--white);
    text-shadow: 0 1px 3px rgba(0, 0, 0, 0.35);
  }
  .service-list {
    position: absolute;
    top: 84px;
    left: 30px;
    width: 520px;
    margin: 0;
    padding: 0;
    list-style: none;
  }
  .service-list li {
    position: relative;
    padding-left: 40px;
    margin-bottom: 17px;
    font-weight: 600;
    font-size: 23px;
    line-height: 27px;
    color: var(--ink);
  }
  .service-list .tick {
    position: absolute;
    left: 0;
    top: 3px;
    width: 24px;
    height: 22px;
  }
  .photo {
    position: absolute;
    left: 601px;
    width: 272px;
    border-radius: 14px;
    border: 2px solid rgba(255, 255, 255, 0.6);
    box-sizing: border-box;
  }
  .photo-hedge-trim {
    top: 13px;
    height: 174px;
    background: linear-gradient(160deg, #9aa27a 0%, #5f8a2e 50%, #3f6d1f 100%);
  }
  .photo-lawn-mower {
    top: 200px;
    height: 182px;
    background: linear-gradient(135deg, #c9d2c6 0%, #4f8f2a 55%, #2f6a1a 100%);
  }
  .photo-pressure-wash {
    top: 392px;
    height: 184px;
    background: linear-gradient(150deg, #8a8f88 0%, #9c6a4a 50%, #6e4a34 100%);
  }
  .contact-heading {
    position: absolute;
    top: 506px;
    left: 30px;
    margin: 0;
    font-family: "Roboto", sans-serif;
    font-weight: 700;
    font-size: 36px;
    line-height: 44px;
    color: var(--white);
    text-shadow: 0 1px 3px rgba(0, 0, 0, 0.35);
  }
  .contact-phones {
    position: absolute;
    top: 556px;
    left: 30px;
    width: 560px;
    margin: 0;
    font-family: "Roboto", sans-serif;
    font-weight: 900;
    font-size: 38px;
    line-height: 46px;
    color: var(--ink);
    white-space: nowrap;
  }
  .contact-email {
    position: absolute;
    top: 612px;
    left: 30px;
    margin: 0;
    font-family: "Roboto", sans-serif;
    font-weight: 700;
    font-size: 26px;
    line-height: 34px;
    color: var(--ink);
  }
  .contact-address {
    position: absolute;
    top: 666px;
    left: 30px;
    margin: 0;
    font-weight: 600;
    font-size: 18px;
    line-height: 26px;
    color: var(--ink);
  }
  .hedge-strip {
    position: absolute;
    left: 0;
    bottom: 0;
    width: 100%;
    height: 210px;
    background: linear-gradient(180deg, rgba(127, 174, 58, 0) 0%, var(--hedge-light) 20%, var(--hedge-dark) 100%);
  }
</style>
</head>
<body>
  <main class="flyer">
    <h1 class="brand-title">BRAMBLEWICK<br>GARDEN SERVICES</h1>
    <div class="tagline-band">Exterior Property Maintenance</div>

    <section class="info-panel">
      <h2 class="services-heading">Our Services</h2>
      <ul class="service-list">
        <li><svg class="tick" viewBox="0 0 24 22" aria-hidden="true"><path d="M2 12 L9 19 L22 3" fill="none" stroke="#111a12" stroke-width="3.2" stroke-linecap="round" stroke-linejoin="round"/></svg>Regular fortnightly visits or one-off garden tidy ups</li>
        <li><svg class="tick" viewBox="0 0 24 22" aria-hidden="true"><path d="M2 12 L9 19 L22 3" fill="none" stroke="#111a12" stroke-width="3.2" stroke-linecap="round" stroke-linejoin="round"/></svg>All kinds of trees expertly felled, topped or pruned</li>
        <li><svg class="tick" viewBox="0 0 24 22" aria-hidden="true"><path d="M2 12 L9 19 L22 3" fill="none" stroke="#111a12" stroke-width="3.2" stroke-linecap="round" stroke-linejoin="round"/></svg>Hedge cutting</li>
        <li><svg class="tick" viewBox="0 0 24 22" aria-hidden="true"><path d="M2 12 L9 19 L22 3" fill="none" stroke="#111a12" stroke-width="3.2" stroke-linecap="round" stroke-linejoin="round"/></svg>Lawn mowing, Pruning, Strimming</li>
        <li><svg class="tick" viewBox="0 0 24 22" aria-hidden="true"><path d="M2 12 L9 19 L22 3" fill="none" stroke="#111a12" stroke-width="3.2" stroke-linecap="round" stroke-linejoin="round"/></svg>Fencing replaced or repaired</li>
        <li><svg class="tick" viewBox="0 0 24 22" aria-hidden="true"><path d="M2 12 L9 19 L22 3" fill="none" stroke="#111a12" stroke-width="3.2" stroke-linecap="round" stroke-linejoin="round"/></svg>Access to fully qualified and licenced tree arborist</li>
        <li><svg class="tick" viewBox="0 0 24 22" aria-hidden="true"><path d="M2 12 L9 19 L22 3" fill="none" stroke="#111a12" stroke-width="3.2" stroke-linecap="round" stroke-linejoin="round"/></svg>Fully Insured</li>
      </ul>

      <div class="photo photo-hedge-trim" role="img" aria-label="Photo of a gardener trimming a hedge with a hedge cutter"></div>
      <div class="photo photo-lawn-mower" role="img" aria-label="Photo of a red lawn mower cutting grass"></div>
      <div class="photo photo-pressure-wash" role="img" aria-label="Photo of block paving being pressure washed"></div>

      <h2 class="contact-heading">Contact us</h2>
      <p class="contact-phones">07724 316048, 01632 742918</p>
      <p class="contact-email">Email: hello@bramblewickgardens.co.uk</p>
      <p class="contact-address">14 Fernlea Close, Oakridge, Hollowford, Cheshire, HF3 8QL</p>
    </section>

    <div class="hedge-strip" role="img" aria-label="Photo of a leafy green hedge along the bottom edge"></div>
  </main>
</body>
</html>
```